Youth Football Center needs modern,elegant Letterhead

Our school needs a modern Letterhead with header a footer for Electronic and Hardcopy. Busuness Cards, Envelopes and Powerpoint template.
The header/footer are to have:
The school name: Torvald Menkes School of Football
School moto - "I think, therefore I am"

Contact details: Address: 17 Lupin Close, Kelmore, Harare, Zimbabwe

Mobiles: +263 77 418 6093, +263 77 530 7186
website (some of these things could be in the footer)
Email: dmenkes@tmqx.org
School website is www.tmqx.org

Registar of Deeds# KT517/2009

Industry/Entity Type

School

Font styles to use
Serif

```html
<!DOCTYPE html>
<html lang="en">
<head>
<meta charset="utf-8">
<title>Torvald Menkes School of Football — Letterhead</title>
<link href="https://fonts.googleapis.com/css2?family=Source+Sans+3:wght@400;600;700&display=swap" rel="stylesheet">
<style>
  :root {
    --backdrop: #5a5a5c;
    --paper: #ffffff;
    --ink: #2b2b2b;
    --rule: #333333;
    --brand-green: #139a48;
    --brand-gold: #f2b51c;
    --brand-red: #b8202a;
    --faint: #f0f0f2;
    --signature-tone: #ececec;
  }
  * { margin: 0; padding: 0; box-sizing: border-box; }
  html, body {
    width: 1200px; height: 999px; overflow: hidden;
    background: var(--backdrop);
    font-family: "Source Sans 3", "Myriad Pro", Arial, sans-serif;
    color: var(--ink);
  }
  .letterhead {
    position: absolute; left: 204px; top: 49px;
    width: 696px; height: 900px;
    background: var(--paper);
    overflow: hidden;
  }
  .brand {
    position: absolute; left: 0; right: 0; top: 88px;
    display: flex; justify-content: center; align-items: center; gap: 8px;
    font-size: 17px; font-weight: 600; color: var(--brand-green);
    letter-spacing: 0.5px;
  }
  .brand-dot {
    width: 12px; height: 12px; border-radius: 50%;
    background: var(--brand-green);
  }
  .header-rule {
    position: absolute; left: 39px; top: 119px;
    width: 628px; height: 3px; background: var(--rule);
  }
  .salutation {
    position: absolute; left: 44px; top: 201px;
    font-size: 12.5px;
  }
  .letter-body {
    position: absolute; left: 44px; top: 283px; width: 607px;
    font-size: 12.5px; line-height: 16.4px; text-align: justify;
  }
  .letter-body p + p { margin-top: 16.4px; }
  .watermark {
    position: absolute; left: 0; top: 596px;
    width: 420px; height: 240px;
    display: flex; align-items: center; justify-content: center; gap: 14px;
  }
  .watermark-mark {
    width: 120px; height: 120px; border-radius: 50%;
    background: var(--faint);
  }
  .watermark-name {
    font-size: 26px; font-weight: 600; color: var(--faint);
    line-height: 1.15; width: 240px;
  }
  .sign-off {
    position: absolute; left: 390px; top: 617px; width: 260px;
    text-align: center; font-size: 12.5px;
  }
  .signature {
    display: block; width: 96px; height: 94px;
    margin: 7px auto 0; background: var(--signature-tone);
    border-radius: 4px;
  }
  .sign-name {
    position: absolute; right: 45px; top: 737px;
    font-size: 12.5px; text-transform: uppercase; white-space: nowrap;
  }
  .footer-band {
    position: absolute; left: 0; bottom: 0; width: 697px; height: 46px;
    background: var(--brand-green); color: #fff;
    font-size: 10.5px; font-weight: 600; text-align: center;
    padding-top: 8px; line-height: 14px;
  }
  .footer-band svg { width: 9px; height: 9px; vertical-align: -1px; fill: #fff; }
</style>
</head>
<body>
  <main class="letterhead">
    <header>
      <div class="brand"><span class="brand-dot"></span>Torvald Menkes School of Football</div>
      <div class="header-rule"></div>
    </header>

    <p class="salutation">Dear Mr Smith</p>

    <section class="letter-body">
      <p>Lorem ipsum dolor sit amet, consectetur adipiscing elit. Sed et mattis nibh, in tincidunt mi. Integer nisl felis, cursus viverra est id, tincidunt lobortis sapien. Phasellus fermentum nisl venenatis tincidunt gravida. Fusce ullamcorper imperdiet est, vitae lacinia libero rutrum non. Ut vehicula, velit at condimentum pellentesque, lorem ligula laoreet lorem, euismod dignissim justo nunc vel ante. Maecenas dui ipsum, posuere in viverra quis, lacinia non arcu. Aliquam aliquam aliquam urna id sollicitudin. Aenean in risus vel nisl tincidunt molestie nec a massa. Vestibulum ante ipsum primis in faucibus orci luctus et ultrices posuere cubilia Curae; Sed consequat interdum venenatis.</p>
      <p>Nam est libero, tincidunt vel nibh eget, egestas sollicitudin purus. Pellentesque consequat neque eu leo consectetur pellentesque. Cras et adipiscing ligula, eget elementum justo. Aliquam suscipit pulvinar enim quis laoreet. Etiam quis eros dignissim justo mattis blandit. Donec erat ligula, aliquet quis leo hendrerit, sagittis lobortis velit. Aliquam turpis mauris, lobortis at convallis quis, luctus vitae turpis. Nam mattis, magna nec iaculis vestibulum, tortor libero posuere dui, vitae condimentum turpis ante quis magna. Sed diam eros, molestie sed massa in, mattis elementum neque. Donec eros velit, tempor eget sem vel, dignissim suscipit nunc. Vestibulum convallis facilisis lacus ac cursus. Nullam vehicula nulla non magna blandit facilisis. Pellentesque vitae semper tellus, ut cursus diam.</p>
    </section>

    <div class="watermark" aria-hidden="true">
      <span class="watermark-mark"></span>
      <span class="watermark-name">Torvald Menkes School of Football</span>
    </div>

    <div class="sign-off">
      Best Regards
      <span class="signature" role="img" aria-label="Handwritten signature"></span>
    </div>
    <p class="sign-name">Torvald Menkes School of Football</p>

    <footer class="footer-band">
      17 Lupin Close, Kelmore, Harare, Zimbabwe<br>
      <svg viewBox="0 0 10 10" aria-hidden="true"><rect x="2.5" y="0" width="5" height="10" rx="1"/></svg>
      +263 77 418 6093, +263 77 530 7186 |
      <svg viewBox="0 0 10 10" aria-hidden="true"><rect x="0" y="2" width="10" height="6.5" rx="0.8"/></svg>
      dmenkes@tmqx.org |
      <svg viewBox="0 0 10 10" aria-hidden="true"><path d="M1 9 L9 1 L6 9 L5 5 Z"/></svg>
      www.tmqx.org
    </footer>
  </main>
</body>
</html>
```